Modern Business Card for Lanternfield 2018

Our company assumes the best about people. We are creating an online community of entrepreneurs and business leaders who struggle with marketing their business online.

This business card should POP! We recently got a new logo and are launching a new website next month, so our business cards should make a statement that feels:
-Fresh
-Smart
-Trustworthy
-Fun

Target Market(s)

small business owners, entrepreneurs

Industry/Entity Type

Digital Marketing

Contact Information for Business Card

Dimensions: 3.5" x 2"

Font styles to use
Sans Serif

Colors
f37122
ffffff

Requirements
Must have
• We need a business card with a modern, bold design. We will use one side of the card as a lead-generation offer, so text on one side will need to fit up to 140 characters. The business card should stick to our core colors (orange, black, and white).
Nice to have
• We think a vertical "portrait" design could be interesting.
Should not have
• Should not look like a traditional business card. The round icon should stand out from a distance.

```html
<!DOCTYPE html>
<html lang="en">
<head>
<meta charset="utf-8">
<title>Lanternfield Business Card</title>
<link rel="stylesheet" href="https://fonts.googleapis.com/css2?family=Raleway:wght@400;500;600;700;800&display=swap">
<style>
  :root {
    --orange: #f26a28;
    --orange-soft: #fce4d9;
    --ink: #222222;
    --white: #ffffff;
    --backdrop: #2b2722;
  }
  * { box-sizing: border-box; margin: 0; padding: 0; }
  html, body {
    width: 1200px; height: 1200px; overflow: hidden;
    background: var(--backdrop);
    font-family: "Raleway", sans-serif;
  }
  .canvas { position: relative; width: 1200px; height: 1200px; }
  .card {
    position: absolute; left: 240px; width: 720px; height: 410px;
    background: var(--white); border-radius: 26px; overflow: hidden;
  }
  .card--front { top: 144px; }
  .card--back { top: 598px; }

  /* Front */
  .front-header {
    position: absolute; top: 0; left: 0; right: 0; height: 113px;
    background: var(--orange); text-align: center; padding-top: 30px;
  }
  .brand-name { font-weight: 800; letter-spacing: 0.5px; line-height: 1; }
  .front-header .brand-name { color: var(--white); font-size: 38px; }
  .tagline { font-weight: 600; color: var(--ink); font-size: 15px; margin-top: 6px; }
  .front-mark {
    position: absolute; left: 256px; top: 136px; width: 208px; height: 208px;
    border-radius: 50%; background: var(--orange-soft);
  }
  .front-url {
    position: absolute; left: 0; right: 0; top: 354px; text-align: center;
    font-size: 17px; letter-spacing: 2.4px; color: var(--ink); font-weight: 500;
  }
  .front-url .accent { color: var(--orange); }
  .front-footer {
    position: absolute; left: 0; right: 0; bottom: 0; height: 25px; background: var(--ink);
  }

  /* Back */
  .back-header {
    position: absolute; top: 0; left: 0; right: 0; height: 113px;
    background: var(--ink); padding: 28px 0 0 25px;
  }
  .person-name { font-size: 36px; font-weight: 700; color: var(--white); line-height: 1; letter-spacing: 0.5px; }
  .person-name .first { color: var(--orange); }
  .person-role { font-size: 18px; font-weight: 500; color: var(--white); margin-top: 8px; }
  .brand-dot {
    position: absolute; left: 504px; top: 32px; width: 144px; height: 144px;
    border-radius: 50%; background: var(--white);
    display: flex; align-items: center; justify-content: center;
  }
  .brand-dot::after {
    content: ""; width: 124px; height: 124px; border-radius: 50%; background: var(--orange);
  }
  .back-brand { position: absolute; right: 26px; top: 184px; text-align: right; }
  .back-brand .brand-name { color: var(--orange); font-size: 42px; }
  .back-brand .tagline { margin-top: 8px; }
  .contact-band {
    position: absolute; left: 0; right: 0; bottom: 0; height: 74px; background: var(--orange);
  }
  .contact-icon {
    position: absolute; top: -17px; width: 34px; height: 34px; border-radius: 50%;
    background: var(--ink); border: 3px solid var(--white);
    display: flex; align-items: center; justify-content: center;
  }
  .contact-icon svg { width: 14px; height: 14px; fill: var(--white); }
  .contact-text {
    position: absolute; top: 22px; font-size: 18px; color: var(--white);
    font-weight: 500; letter-spacing: 0.8px; white-space: nowrap;
  }
</style>
</head>
<body>
<div class="canvas">
  <section class="card card--front">
    <header class="front-header">
      <div class="brand-name">LANTERNFIELD</div>
      <div class="tagline">Tell stories that inspire action</div>
    </header>
    <div class="front-mark" aria-hidden="true"></div>
    <div class="front-url">www.<span class="accent">lanternfieldnow</span>.com</div>
    <div class="front-footer"></div>
  </section>

  <section class="card card--back">
    <header class="back-header">
      <div class="person-name"><span class="first">MILES</span> HARTWELL</div>
      <div class="person-role">Story Marketing Coach</div>
    </header>
    <div class="brand-dot" aria-hidden="true"></div>
    <div class="back-brand">
      <div class="brand-name">LANTERNFIELD</div>
      <div class="tagline">Tell stories that inspire action</div>
    </div>
    <footer class="contact-band">
      <span class="contact-icon" style="left:24px">
        <svg viewBox="0 0 24 24"><path d="M6.6 10.8a15.1 15.1 0 0 0 6.6 6.6l2.2-2.2c.3-.3.7-.4 1-.2 1.1.4 2.3.6 3.6.6.6 0 1 .4 1 1V20c0 .6-.4 1-1 1A17 17 0 0 1 3 4c0-.6.4-1 1-1h3.5c.6 0 1 .4 1 1 0 1.3.2 2.5.6 3.6.1.3 0 .7-.2 1z"/></svg>
      </span>
      <span class="contact-icon" style="left:294px">
        <svg viewBox="0 0 24 24"><path d="M2 11.5 21 4l-3 16-6-4.5-3 3v-4.5l9-8-11 7z"/></svg>
      </span>
      <span class="contact-icon" style="left:567px">
        <svg viewBox="0 0 24 24"><path d="M5 3l14 7-6 2 5 6-2 2-5-6-3 5z"/></svg>
      </span>
      <span class="contact-text" style="left:25px">000.000.0000</span>
      <span class="contact-text" style="left:160px">miles@lanternfieldnow.com</span>
      <span class="contact-text" style="right:24px">www.lanternfieldnow.com</span>
    </footer>
  </section>
</div>
</body>
</html>
```